Zephyrant Climate Crew WA Truck

I want a truck desing that screams Professional, Friendly and serious about work. you can find some of our work on our website, facebook and instagram.
https://zephyrantcrew.example.com.au/
https://www.instagram.com/zphcrewox/
https://www.facebook.com/profile.php?id=70318825094631

The design needs to include our refrigeration license: AU38452 and electrical License: EC94031
I want the colours to be consistent with my Logo.

Key Notes to be included in the design, I want to let people know we do the following;
- Commercial and Residential
- Repairs, Service and Installation
- Reverse cycle ducted Air Conditioning
- Wall Split Air Conditioning
- Ceiling Cassettes
- Evaporative Air Conditioning
- Cool Rooms
- Display Fridges
- Beer Chillers

```html
<!DOCTYPE html>
<html lang="en">
<head>
<meta charset="utf-8">
<title>Zephyrant Climate Crew WA – Truck Side Panel</title>
<link rel="stylesheet" href="https://fonts.googleapis.com/css2?family=Oswald:wght@300;400;500;600&display=swap">
<style>
  :root {
    --canvas: #ffffff;
    --photo-dark: #26272b;
    --photo-mid: #34363b;
    --navy: #1b2f5e;
    --blue: #1a64a8;
    --orange-red: #e5471a;
    --orange: #f39a2c;
    --yellow: #f7b233;
    --white: #ffffff;
  }
  html, body {
    margin: 0;
    padding: 0;
    width: 1200px;
    height: 1188px;
    overflow: hidden;
    background: var(--canvas);
  }
  .truck-panel {
    position: absolute;
    left: 0;
    top: 316px;
    width: 1200px;
    height: 556px;
    display: block;
  }
  .services-title { font-family: "Oswald", sans-serif; font-weight: 600; font-size: 46px; fill: var(--white); }
  .service-item { font-family: "Oswald", sans-serif; font-weight: 300; font-size: 21px; fill: var(--white); }
  .tick { fill: none; stroke: var(--white); stroke-width: 2.4; stroke-linecap: round; stroke-linejoin: round; }
  .licence-number { font-family: "Oswald", sans-serif; font-weight: 400; font-size: 27px; fill: var(--white); }
  .licence-icon { fill: none; stroke: var(--white); stroke-width: 2.4; }
  .phone-number { font-family: "Oswald", sans-serif; font-weight: 500; font-size: 42px; fill: var(--white); }
  .email { font-family: "Oswald", sans-serif; font-weight: 400; font-size: 14px; fill: var(--white); }
  .icon-fill { fill: var(--white); }
  .brand-name { font-family: "Oswald", sans-serif; font-weight: 600; fill: var(--orange); letter-spacing: 1px; }
</style>
</head>
<body>
<svg class="truck-panel" viewBox="0 0 1208 560" xmlns="http://www.w3.org/2000/svg">
  <defs>
    <linearGradient id="photoTone" x1="0" y1="0" x2="1" y2="1">
      <stop offset="0" stop-color="var(--photo-mid)"/>
      <stop offset="1" stop-color="var(--photo-dark)"/>
    </linearGradient>
    <linearGradient id="orangeSweep" x1="0" y1="0" x2="1" y2="0.6">
      <stop offset="0" stop-color="var(--orange-red)"/>
      <stop offset="1" stop-color="var(--yellow)"/>
    </linearGradient>
    <linearGradient id="blueField" x1="0" y1="0" x2="0.6" y2="1">
      <stop offset="0" stop-color="var(--navy)"/>
      <stop offset="1" stop-color="var(--blue)"/>
    </linearGradient>
    <linearGradient id="rightSweep" x1="0" y1="0" x2="0" y2="1">
      <stop offset="0" stop-color="var(--yellow)"/>
      <stop offset="1" stop-color="var(--orange-red)"/>
    </linearGradient>
    <linearGradient id="rightBlue" x1="0" y1="0" x2="0" y2="1">
      <stop offset="0" stop-color="var(--navy)"/>
      <stop offset="1" stop-color="var(--blue)"/>
    </linearGradient>
  </defs>

  <rect class="technician-photo" x="0" y="0" width="1208" height="560" fill="url(#photoTone)"
        role="img" aria-label="Darkened photo of an air conditioning technician servicing an outdoor unit"/>

  <path d="M0,0 C380,0 640,210 698,560 L0,560 Z" fill="var(--white)"/>
  <path d="M0,8 C340,22 560,180 650,420 L650,560 L0,560 Z" fill="url(#orangeSweep)"/>
  <path d="M0,86 C310,80 570,210 682,560 L0,560 Z" fill="url(#blueField)"/>

  <path d="M1172,0 L1208,0 L1208,560 L976,560 C1090,420 1162,230 1172,0 Z" fill="var(--white)"/>
  <path d="M1180,0 L1208,0 L1208,560 L992,560 C1106,420 1176,230 1180,0 Z" fill="url(#rightSweep)"/>
  <path d="M1208,170 L1208,560 L1058,560 C1140,450 1190,320 1208,170 Z" fill="url(#rightBlue)"/>

  <g class="brand">
    <circle cx="855" cy="180" r="30" fill="var(--orange)"/>
    <text class="brand-name" x="855" y="262" font-size="40" text-anchor="middle">ZEPHYRANT</text>
    <text class="brand-name" x="855" y="298" font-size="24" text-anchor="middle">CLIMATE CREW WA</text>
  </g>

  <text class="services-title" x="60" y="186">Services</text>
  <g class="service-list">
    <path class="tick" d="M62,222 l6,6 l12,-12"/><text class="service-item" x="92" y="227">Commercial and Residential</text>
    <path class="tick" d="M62,250 l6,6 l12,-12"/><text class="service-item" x="92" y="255">Repairs, Service and Installation</text>
    <path class="tick" d="M62,279 l6,6 l12,-12"/><text class="service-item" x="92" y="284">Reverse cycle ducted Air Conditioning</text>
    <path class="tick" d="M62,307 l6,6 l12,-12"/><text class="service-item" x="92" y="312">Wall Split Air Conditioning</text>
    <path class="tick" d="M62,336 l6,6 l12,-12"/><text class="service-item" x="92" y="341">Ceiling Cassettes</text>
    <path class="tick" d="M62,364 l6,6 l12,-12"/><text class="service-item" x="92" y="369">Evaporative Air Conditioning</text>
    <path class="tick" d="M62,393 l6,6 l12,-12"/><text class="service-item" x="92" y="398">Cool Rooms</text>
    <path class="tick" d="M62,421 l6,6 l12,-12"/><text class="service-item" x="92" y="426">Display Fridges</text>
    <path class="tick" d="M62,450 l6,6 l12,-12"/><text class="service-item" x="92" y="455">Beer Chillers</text>
  </g>

  <g class="licences">
    <path class="licence-icon" d="M82,536 L60,536 L60,486 L94,486 L94,512"/>
    <line class="licence-icon" x1="67" y1="498" x2="87" y2="498"/>
    <line class="licence-icon" x1="67" y1="507" x2="87" y2="507"/>
    <line class="licence-icon" x1="67" y1="516" x2="78" y2="516"/>
    <circle class="licence-icon" cx="94" cy="524" r="7"/>
    <path class="licence-icon" d="M90,531 L90,542 L94,538 L98,542 L98,531"/>
    <text class="licence-number" x="120" y="506">AU38452</text>
    <text class="licence-number" x="120" y="538">EC94031</text>
  </g>

  <g class="contact">
    <path class="icon-fill" d="M306,488 c3,-2 6,-2 7,0 l4,7 c1,2 0,4 -2,5 l-2,1 c1,4 4,8 8,11 l2,-2 c2,-1 4,-1 5,1 l4,6 c1,2 0,4 -2,5 c-3,2 -6,2 -9,1 c-8,-4 -15,-12 -18,-21 c-1,-5 0,-11 3,-14 z"/>
    <text class="phone-number" x="343" y="514">0400 555 318</text>
    <rect class="icon-fill" x="306" y="524" width="14" height="10" rx="1"/>
    <path d="M306,524 L313,530 L320,524" fill="none" stroke="var(--navy)" stroke-width="1.4"/>
    <text class="email" x="343" y="534">info@zephyrantcrew.example.com.au</text>
  </g>
</svg>
</body>
</html>
```